We have over 30 years of experience in various construction projects. New additions, rehab work, interior and exterior etc. We started our own company about a year ago.
I am attaching a card that I received from a client that I really like and would like to follow as a template, but I am very open to your creative approach. I am interested in my logo (which will be later used for my website) to incorporate the "M&P" or "M&P Remodeling" Please email me at mpremodeling 81@brindlemail.com or call Walt at 773-555-0182.

Industry/Entity Type

Construction

Contact Information for Business Card

M&P Remodeling and Beacon Services
2816 W Oakridge Ave
Elmdale, IL 60799
708-555-0147 - Polish
708-555-0163 - English

Piotr Walek - Owner
Marek WAlek Jr - Construction Manager
mpremodeling81@brindlemail.com

```html
<!DOCTYPE html>
<html lang="en">
<head>
<meta charset="utf-8">
<title>M&amp;P Remodeling and Beacon Services – Business Card</title>
<link rel="stylesheet" href="https://fonts.googleapis.com/css2?family=Open+Sans:wdth,wght@75..100,400;75..100,600&display=swap">
<style>
  :root {
    --page-bg: #eceeee;
    --card-brown: #3f2f23;
    --card-brown-light: #4a382b;
    --text-light: #f1eeea;
    --mark-silver: #cdc7bf;
    --divider: #b9afa5;
  }
  * { margin: 0; padding: 0; box-sizing: border-box; }
  html, body {
    width: 1031px; height: 1200px; overflow: hidden;
    background: var(--page-bg);
    font-family: "Open Sans", Arial, sans-serif;
    font-stretch: 75%;
    color: var(--text-light);
  }
  .card {
    position: absolute;
    left: 149px;
    width: 786px;
    height: 474px;
    background: radial-gradient(ellipse at 50% 40%, var(--card-brown-light), var(--card-brown));
  }
  .card--front { top: 76px; }
  .card--back { top: 628px; }

  .brand-name {
    position: absolute;
    font-weight: 400;
    color: var(--mark-silver);
    line-height: 1;
    white-space: nowrap;
  }
  .card--front .brand-name { left: 46px; top: 103px; font-size: 225px; letter-spacing: -5px; }
  .card--back .brand-name { left: 158px; top: 30px; font-size: 120px; letter-spacing: -3px; }

  .tagline {
    position: absolute;
    white-space: nowrap;
    font-weight: 400;
    line-height: 1;
  }
  .card--front .tagline { left: 290px; top: 378px; font-size: 30px; }
  .card--back .tagline { left: 347px; top: 149px; font-size: 21px; }

  .people, .contacts {
    position: absolute;
    top: 236px;
    font-size: 27px;
    line-height: 43px;
    white-space: nowrap;
  }
  .people { right: calc(786px - 282px); text-align: right; }
  .contacts { left: 346px; }
  .person-name, .phone-number { font-weight: 600; }
  .divider {
    position: absolute;
    left: 308px; top: 250px;
    width: 2px; height: 154px;
    background: var(--divider);
  }
</style>
</head>
<body>
  <section class="card card--front">
    <div class="brand-name">M&amp;P</div>
    <div class="tagline">M&amp;P Remodeling and Beacon Services</div>
  </section>

  <section class="card card--back">
    <div class="brand-name">M&amp;P</div>
    <div class="tagline">M&amp;P Remodeling and Beacon Services</div>

    <div class="people">
      <div class="person-name">Piotr Walek</div>
      <div class="person-role">Owner</div>
      <div class="person-name">Marek Walek</div>
      <div class="person-role">Construction Manager</div>
    </div>
    <div class="divider"></div>
    <div class="contacts">
      <div><span class="phone-number">708-555-0147</span> - Polish</div>
      <div><span class="phone-number">708-555-0163</span> - English</div>
      <div>mpremodeling81@brindlemail.com</div>
      <div>2816 W Oakridge Ave Elmdale, IL 60799</div>
    </div>
  </section>
</body>
</html>
```